Bref créative
Stationery design for KORV Holdings
KORV Holdings - Motion Lessons & Media
Use same font as used in my logo
Trajan Bold
Bright & Fun-filled
Damian Whitcombe
IT & Technical Support
The Lumley House
12 Fenwick Lane
Ashcombe-Under-Lyne
Bristol
BS4 7QD
damian@korv.co
www.korv.co
This is the KORV Holdings logo.

```html
<!DOCTYPE html>
<html lang="en">
<head>
<meta charset="utf-8">
<title>KORV Holdings – Business Card</title>
<link rel="stylesheet" href="https://fonts.googleapis.com/css2?family=Cinzel:wght@400;700&display=swap">
<style>
  :root {
    --backdrop: #b9b9bb;
    --gold-deep: #c59c17;
    --gold-light: #e2be2f;
    --gold-text: #b8901c;
    --ink-soft: #8a7a4a;
    --paper: #fbfbf9;
    --white: #ffffff;
  }
  * { margin: 0; padding: 0; box-sizing: border-box; }
  html, body {
    width: 1200px; height: 895px; overflow: hidden;
    background: var(--backdrop);
    font-family: "Cinzel", "Times New Roman", serif;
  }
  .canvas {
    width: 1200px; height: 895px;
    display: flex; flex-direction: column; align-items: center; justify-content: center;
    gap: 40px;
  }
  .card {
    width: 680px; height: 388px;
    position: relative;
    box-shadow: 0 6px 18px rgba(0,0,0,0.18);
  }
  /* Front */
  .card-front {
    background: linear-gradient(135deg, var(--gold-light) 0%, var(--gold-deep) 100%);
    display: flex; flex-direction: column; align-items: center; justify-content: center;
    color: var(--white);
  }
  .front-name {
    font-weight: 700; font-size: 96px; letter-spacing: 4px; line-height: 1;
  }
  .front-web {
    margin-top: 22px; font-size: 15px; letter-spacing: 7px; text-transform: uppercase;
  }
  /* Back */
  .card-back {
    background: var(--paper);
    padding: 56px 60px;
    color: var(--gold-text);
  }
  .brand-name {
    font-weight: 700; font-size: 52px; letter-spacing: 3px; line-height: 1;
    text-transform: uppercase; color: var(--gold-text);
  }
  .person {
    margin-top: 26px; font-size: 17px; letter-spacing: 1px; color: var(--gold-text);
  }
  .person .role { color: var(--ink-soft); }
  .contacts { margin-top: 28px; display: flex; flex-direction: column; gap: 9px; }
  .contact-row { display: flex; gap: 22px; flex-wrap: wrap; }
  .contact {
    display: flex; align-items: center; gap: 7px;
    font-size: 12px; letter-spacing: 0.8px; color: var(--ink-soft); text-transform: uppercase;
  }
  .contact svg { width: 14px; height: 14px; flex: none; }
</style>
</head>
<body>
<main class="canvas">
  <section class="card card-front">
    <div class="front-name">KORV</div>
    <div class="front-web">www.korv.co</div>
  </section>

  <section class="card card-back">
    <div class="brand-name">KORV Holdings</div>
    <p class="person">Damian Whitcombe <span class="role">| IT &amp; Technical Support</span></p>
    <div class="contacts">
      <div class="contact-row">
        <span class="contact">
          <svg viewBox="0 0 14 14"><circle cx="7" cy="7" r="7" fill="#c59c17"/><path d="M7 3.2a2.4 2.4 0 0 0-2.4 2.4C4.6 7.4 7 10.6 7 10.6s2.4-3.2 2.4-5A2.4 2.4 0 0 0 7 3.2z" fill="#fff"/></svg>
          12 Fenwick Lane, Ashcombe-Under-Lyne, Bristol, BS4 7QD
        </span>
      </div>
      <div class="contact-row">
        <span class="contact">
          <svg viewBox="0 0 14 14"><circle cx="7" cy="7" r="7" fill="#c59c17"/><path d="M4.6 3.8l1.3-.3.7 1.7-.8.6a5 5 0 0 0 2.4 2.4l.6-.8 1.7.7-.3 1.3c-3.3 0-5.9-2.6-5.6-5.6z" fill="#fff"/></svg>
          0800 24 71 300
        </span>
        <span class="contact">
          <svg viewBox="0 0 14 14"><circle cx="7" cy="7" r="7" fill="#c59c17"/><rect x="5" y="3.2" width="4" height="7.6" rx="0.8" fill="#fff"/></svg>
          07700 900 482
        </span>
        <span class="contact">
          <svg viewBox="0 0 14 14"><circle cx="7" cy="7" r="7" fill="#c59c17"/><rect x="3.8" y="4.6" width="6.4" height="5" fill="#fff"/></svg>
          0800 24 71 310
        </span>
      </div>
      <div class="contact-row">
        <span class="contact">
          <svg viewBox="0 0 14 14"><circle cx="7" cy="7" r="7" fill="#c59c17"/><circle cx="7" cy="7" r="3.3" fill="none" stroke="#fff" stroke-width="1"/><path d="M3.7 7h6.6" stroke="#fff" stroke-width="1"/></svg>
          www.korv.co
        </span>
        <span class="contact">
          <svg viewBox="0 0 14 14"><circle cx="7" cy="7" r="7" fill="#c59c17"/><rect x="3.6" y="4.6" width="6.8" height="4.8" fill="#fff"/><path d="M3.6 4.6L7 7.4l3.4-2.8" fill="none" stroke="#c59c17" stroke-width="0.8"/></svg>
          damian@korv.co
        </span>
      </div>
    </div>
  </section>
</main>
</body>
</html>
```